Life insurance company website and landing page

Web design is required for life insurance company. Specifically the company will 1) generate leads and 2) provide a blog. The target market of this business is people in their 50s and 60s, medium-high to high income earners, who are likely to have a policy in place already but want to save money on their premiums. Please read the attached design brief for more guidance. Open to any concepts that might work.The outputs for this job will include:1) a website2) a landing page3) fixing logos into a more useful and professional format (this should take 5 mins with the correct software)
Colors
Designer to choose colors to be used in the design.
Look and feel
Each slider illustrates characteristics of the customer's brand and the style your logo design should communicate.

```html
<!DOCTYPE html>
<html lang="en">
<head>
<meta charset="utf-8">
<title>CoverCompare.life — Compare Life Insurers</title>
<link href="https://fonts.googleapis.com/css2?family=Outfit:wght@300;400;500;600&display=swap" rel="stylesheet">
<style>
:root{
  --navy:#0c0b50;
  --lavender:#c3b3fa;
  --lavender-soft:#ecebfd;
  --cyan-soft:#dffcfb;
  --peach-soft:#fdf0ea;
  --pink-soft:#fbe9f2;
  --text:#3a3a55;
  --muted:#77778f;
  --panel:#f3f3f3;
  --line:#d6d6e0;
  --coral:#f4736d;
  --sky:#42c6ef;
  --blue:#4b7cf2;
  --footer:#f5f6fd;
}
*{box-sizing:border-box;margin:0;padding:0}
html,body{width:1200px;height:4127px;overflow:hidden}
body{position:relative;background:#fff;font-family:"Outfit",sans-serif;color:var(--navy)}
.abs{position:absolute}
.bg-svg{position:absolute;left:0;top:0}

/* header */
.brand{display:flex;align-items:center;gap:8px;font-size:13px;color:var(--navy)}
.brand-mark{width:18px;height:18px;border:2px solid var(--coral);border-radius:3px}
.nav a{font-size:11px;color:var(--navy);text-decoration:none;position:absolute;top:40px}
.cta-link{font-size:9px;color:var(--navy)}
.contact-btn{background:var(--lavender-soft);color:#5a4fd0;font-size:9px;display:flex;align-items:center;justify-content:center}

/* hero */
.hero-title{font-size:38px;font-weight:400;line-height:40px;letter-spacing:-.3px}
.hero-sub{font-size:11px;color:var(--text)}
.btn-dark{background:var(--navy);color:#fff;font-size:10px;font-weight:500;display:flex;align-items:center;justify-content:center}
.photo{display:block}

/* partners */
.partner{font-size:15px;font-weight:600;color:var(--navy);display:flex;align-items:center;gap:6px;transform:translateX(-50%)}
.partner .dot{width:10px;height:10px;border-radius:50%;background:var(--lavender)}

/* chart */
.chart-panel{background:var(--panel);box-shadow:0 24px 40px rgba(20,20,60,.08)}
.chart-label{font-size:9px;font-weight:500;text-anchor:end;fill:var(--navy)}
.axis-label{font-size:8px;font-weight:600;text-anchor:middle;fill:var(--navy)}
.section-title{font-size:31px;font-weight:500;line-height:35px}
.body-copy{font-size:12.5px;line-height:19px;color:var(--text)}

/* benefits */
.benefit-icon{width:62px;height:62px;display:flex;align-items:center;justify-content:center}
.benefit-title{font-size:14px;font-weight:500}
.benefit-text{font-size:9.5px;line-height:14px;color:var(--text)}

/* blog */
.blog-card{background:#fff;box-shadow:0 10px 28px rgba(20,20,60,.08)}
.blog-card .thumb{height:299px}
.blog-title{font-size:12.5px;font-weight:500;line-height:17px;padding:13px 11px 0}
.blog-date{font-size:10px;color:var(--muted);padding:0 11px;position:absolute;top:379px}

/* testimonial */
.quote-name{font-size:12px;font-weight:600}
.quote-role{font-size:11px;color:#5a4fd0}

/* contact */
.contact-card{background:#fff;box-shadow:0 16px 40px rgba(20,20,60,.08)}
.field{position:absolute;height:42px;border:1px solid #b9b9c8;font-size:10.5px;color:var(--text);padding-left:12px;display:flex;align-items:center}
.send-btn{font-size:12px}

/* footer */
.footer-bg{background:var(--footer)}
.footer-link{font-size:8.5px;color:var(--text);transform:translateX(-50%)}
.social{width:12px;height:12px;border-radius:50%;background:var(--navy);transform:translateX(-50%)}
.copyright{font-size:7px;color:#a7a7b8;transform:translateX(-50%)}
</style>
</head>
<body>

<!-- decorative backgrounds -->
<svg class="bg-svg" width="1200" height="4127" viewBox="0 0 1200 4127" aria-hidden="true">
  <defs>
    <linearGradient id="heroGrad" x1="0" y1="0" x2="1" y2="1">
      <stop offset="0" stop-color="#dcfcfb"/><stop offset=".7" stop-color="#eefbf6"/><stop offset="1" stop-color="#fdeee8"/>
    </linearGradient>
    <linearGradient id="benefitGrad" x1="0" y1="0" x2="1" y2="1">
      <stop offset="0" stop-color="#dcfcfa"/><stop offset=".65" stop-color="#ebfbf6"/><stop offset="1" stop-color="#fdeee8"/>
    </linearGradient>
    <linearGradient id="quoteGrad" x1="0" y1="0" x2="1" y2="1">
      <stop offset="0" stop-color="#fdeee6"/><stop offset="1" stop-color="#fbe7f3"/>
    </linearGradient>
  </defs>
  <polygon points="0,0 815,0 815,568 0,525" fill="url(#heroGrad)"/>
  <polygon points="0,1413 1200,1450 1200,1871 0,1826" fill="url(#benefitGrad)"/>
  <polygon points="336,2614 1200,2660 1200,3159 336,3116" fill="url(#quoteGrad)"/>
  <rect x="0" y="3305" width="737" height="384" fill="#e9f6fc"/>
  <!-- hero photo frame -->
  <polyline points="692,139 675,139 675,524 961,541 961,529" fill="none" stroke="var(--navy)" stroke-width="1.5"/>
  <!-- testimonial frame -->
  <polyline points="199,2687 173,2687 173,3095 500,3076 500,3060" fill="none" stroke="var(--navy)" stroke-width="1.5"/>
  <!-- dot grids -->
  <g fill="#9b97b8">
    <circle cx="989" cy="252" r="1.6"/><circle cx="1001" cy="252" r="1.6"/><circle cx="1013" cy="252" r="1.6"/>
    <circle cx="989" cy="267" r="1.6"/><circle cx="1001" cy="267" r="1.6"/><circle cx="1013" cy="267" r="1.6"/>
    <circle cx="989" cy="282" r="1.6"/><circle cx="1001" cy="282" r="1.6"/><circle cx="1013" cy="282" r="1.6"/>
    <circle cx="989" cy="297" r="1.6"/><circle cx="1001" cy="297" r="1.6"/><circle cx="1013" cy="297" r="1.6"/>
    <circle cx="989" cy="312" r="1.6"/><circle cx="1001" cy="312" r="1.6"/><circle cx="1013" cy="312" r="1.6"/>
    <circle cx="989" cy="327" r="1.6"/><circle cx="1001" cy="327" r="1.6"/><circle cx="1013" cy="327" r="1.6"/>
    <circle cx="989" cy="342" r="1.6"/><circle cx="1001" cy="342" r="1.6"/><circle cx="1013" cy="342" r="1.6"/>
    <circle cx="989" cy="357" r="1.6"/><circle cx="1001" cy="357" r="1.6"/><circle cx="1013" cy="357" r="1.6"/>
    <circle cx="989" cy="372" r="1.6"/><circle cx="1001" cy="372" r="1.6"/><circle cx="1013" cy="372" r="1.6"/>
  </g>
  <g fill="#4a4a66">
    <circle cx="1017" cy="3405" r="1.8"/><circle cx="1030" cy="3405" r="1.8"/><circle cx="1043" cy="3405" r="1.8"/>
    <circle cx="1017" cy="3422" r="1.8"/><circle cx="1030" cy="3422" r="1.8"/><circle cx="1043" cy="3422" r="1.8"/>
    <circle cx="1017" cy="3439" r="1.8"/><circle cx="1030" cy="3439" r="1.8"/><circle cx="1043" cy="3439" r="1.8"/>
    <circle cx="1017" cy="3456" r="1.8"/><circle cx="1030" cy="3456" r="1.8"/><circle cx="1043" cy="3456" r="1.8"/>
    <circle cx="1017" cy="3473" r="1.8"/><circle cx="1030" cy="3473" r="1.8"/><circle cx="1043" cy="3473" r="1.8"/>
    <circle cx="1017" cy="3490" r="1.8"/><circle cx="1030" cy="3490" r="1.8"/><circle cx="1043" cy="3490" r="1.8"/>
    <circle cx="1017" cy="3507" r="1.8"/><circle cx="1030" cy="3507" r="1.8"/><circle cx="1043" cy="3507" r="1.8"/>
    <circle cx="1017" cy="3524" r="1.8"/><circle cx="1030" cy="3524" r="1.8"/><circle cx="1043" cy="3524" r="1.8"/>
    <circle cx="1017" cy="3541" r="1.8"/><circle cx="1030" cy="3541" r="1.8"/><circle cx="1043" cy="3541" r="1.8"/>
  </g>
</svg>

<!-- header -->
<header>
  <div class="brand abs" style="left:178px;top:38px"><span class="brand-mark"></span>CoverCompare.life</div>
  <nav class="nav">
    <a style="left:530px">Home</a>
    <a style="left:583px">Services</a>
    <a style="left:648px">Blog</a>
  </nav>
  <div class="cta-link abs" style="left:839px;top:45px">Compare Quotes Now</div>
  <div class="contact-btn abs" style="left:940px;top:34px;width:86px;height:30px">Contact Us</div>
</header>

<!-- hero -->
<section class="hero">
  <h1 class="hero-title abs" style="left:183px;top:183px">Compare Australia's<br>Leading Life<br>Insurers Free Today</h1>
  <p class="hero-sub abs" style="left:183px;top:326px">Make sure your insurer isn't charging you too much</p>
  <div class="btn-dark abs" style="left:183px;top:364px;width:150px;height:44px">Compare Quotes Now</div>
  <div class="photo abs" role="img" aria-label="Photo of a smiling family of four leaning on a sofa"
       style="left:692px;top:125px;width:288px;height:404px;background:linear-gradient(160deg,#c9ccd6,#8a7f7a 55%,#3f4450)"></div>
</section>

<!-- partners -->
<section class="partners">
  <div class="partner abs" style="left:195px;top:656px">Tallow</div>
  <div class="partner abs" style="left:301px;top:656px">Meridian</div>
  <div class="partner abs" style="left:407px;top:656px">Zenith</div>
  <div class="partner abs" style="left:511px;top:656px">Novus</div>
  <div class="partner abs" style="left:634px;top:656px"><span class="dot"></span>Metrica</div>
  <div class="partner abs" style="left:772px;top:656px">Harbourline</div>
  <div class="partner abs" style="left:911px;top:656px">Clearpoint</div>
</section>

<!-- pricing chart -->
<section class="pricing">
  <div class="chart-panel abs" style="left:170px;top:830px;width:511px;height:368px"></div>
  <svg class="abs" style="left:0;top:0" width="1200" height="1200" viewBox="0 0 1200 1200" aria-label="Bar chart of premium prices by insurer">
    <g stroke="var(--line)" stroke-width="1">
      <line x1="311" y1="865" x2="311" y2="1148"/><line x1="379" y1="865" x2="379" y2="1148"/>
      <line x1="448" y1="865" x2="448" y2="1148"/><line x1="517" y1="865" x2="517" y2="1148"/>
      <line x1="585" y1="865" x2="585" y2="1148"/><line x1="654" y1="865" x2="654" y2="1148"/>
    </g>
    <line x1="242" y1="865" x2="242" y2="1148" stroke="var(--line)"/>
    <rect x="242" y="866" width="263" height="23" fill="var(--navy)"/>
    <rect x="242" y="902" width="189" height="23" fill="var(--lavender)"/>
    <rect x="242" y="939" width="367" height="23" fill="var(--navy)"/>
    <rect x="242" y="976" width="224" height="23" fill="var(--lavender)"/>
    <rect x="242" y="1011" width="155" height="23" fill="var(--navy)"/>
    <rect x="242" y="1048" width="407" height="23" fill="var(--lavender)"/>
    <rect x="242" y="1085" width="380" height="23" fill="var(--navy)"/>
    <rect x="242" y="1120" width="224" height="23" fill="var(--lavender)"/>
    <text class="chart-label" x="235" y="881">Clearpoint</text>
    <text class="chart-label" x="235" y="917">Meridian</text>
    <text class="chart-label" x="235" y="954">Metrica</text>
    <text class="chart-label" x="235" y="991">Onward</text>
    <text class="chart-label" x="235" y="1026">Harbourline</text>
    <text class="chart-label" x="235" y="1063">Tallow</text>
    <text class="chart-label" x="235" y="1100">Aster</text>
    <text class="chart-label" x="235" y="1135">Zenith</text>
    <text class="axis-label" x="314" y="1161">5K</text>
    <text class="axis-label" x="380" y="1161">10K</text>
    <text class="axis-label" x="450" y="1161">15K</text>
    <text class="axis-label" x="516" y="1161">20K</text>
    <text class="axis-label" x="591" y="1161">25K</text>
    <text class="axis-label" x="654" y="1161">30K</text>
  </svg>
  <h2 class="section-title abs" style="left:737px;top:932px">Price From Different<br>Insurances</h2>
  <p class="body-copy abs" style="left:737px;top:1020px;width:300px">Lorem ipsum dolor sit amet, consetetur sadipscing elitr, sed diam nonumy eirmod tempor invidunt ut labore et dolore magna aliquyam erat, sed diam voluptua. At vero eos</p>
</section>

<!-- benefits -->
<section class="benefits">
  <h2 class="abs" style="left:202px;top:1506px;font-size:26px;font-weight:500">3 Key Benefits -</h2>

  <div class="benefit-icon abs" style="left:202px;top:1587px;background:var(--coral)">
    <svg width="30" height="30" viewBox="0 0 24 24" fill="none" stroke="#fff" stroke-width="1.6"><path d="M12 3l2.6 5.4 5.9.8-4.3 4.1 1 5.8L12 16.4 6.8 19.1l1-5.8L3.5 9.2l5.9-.8z"/></svg>
  </div>
  <div class="benefit-icon abs" style="left:529px;top:1587px;background:var(--sky)">
    <svg width="30" height="30" viewBox="0 0 24 24" fill="none" stroke="#fff" stroke-width="1.6"><path d="M12 3l7 3v5c0 4.5-3 8-7 10-4-2-7-5.5-7-10V6z"/><path d="M9 12l2 2 4-4"/></svg>
  </div>
  <div class="benefit-icon abs" style="left:830px;top:1587px;background:var(--blue)">
    <svg width="30" height="30" viewBox="0 0 24 24" fill="none" stroke="#fff" stroke-width="1.6"><path d="M2 12s4-6 10-6 10 6 10 6-4 6-10 6S2 12 2 12z"/><circle cx="12" cy="12" r="3"/><line x1="4" y1="20" x2="20" y2="4"/></svg>
  </div>

  <h3 class="benefit-title abs" style="left:202px;top:1674px">Australia's Most Trusted Brands</h3>
  <p class="benefit-text abs" style="left:202px;top:1703px;width:200px">You can be confident in that your insurer will be there for you, and your family, when you need them the most</p>
  <h3 class="benefit-title abs" style="left:529px;top:1674px">Price Beat Guarantee</h3>
  <p class="benefit-text abs" style="left:529px;top:1703px;width:180px">We guarantee to beat any quote for a comparable level of cover must be a</p>
  <h3 class="benefit-title abs" style="left:830px;top:1674px">No Hidden Fees</h3>
  <p class="benefit-text abs" style="left:830px;top:1703px;width:200px">Simple pricing that is easy to understand. No hidden fees or charges</p>
</section>

<!-- blog -->
<section class="blog">
  <h2 class="abs" style="left:202px;top:1968px;font-size:26px;font-weight:500">Our Latest Blog</h2>
  <article class="blog-card abs" style="left:199px;top:2051px;width:245px;height:398px">
    <div class="thumb" role="img" aria-label="Photo of two people shaking hands over a desk with laptops and papers" style="background:linear-gradient(150deg,#3b2f2a,#8a6d57 50%,#d8d6d4)"></div>
    <h3 class="blog-title">What's the difference between indemnity value and agreed value insurance?</h3>
    <p class="blog-date">22 September 2019</p>
  </article>
  <article class="blog-card abs" style="left:477px;top:2051px;width:245px;height:398px">
    <div class="thumb" role="img" aria-label="Photo of an open laptop seen from above" style="background:linear-gradient(180deg,#cfcfcf,#e6e6e6 60%,#bdbdbd)"></div>
    <h3 class="blog-title">Life insurance and financial security for singles</h3>
    <p class="blog-date">22 September 2019</p>
  </article>
  <article class="blog-card abs" style="left:750px;top:2051px;width:245px;height:398px">
    <div class="thumb" role="img" aria-label="Photo of a driver sitting in a vintage turquoise pickup truck" style="background:linear-gradient(150deg,#3a4550,#5fb5c2 50%,#c8d8dc)"></div>
    <h3 class="blog-title">Life Insurance and Income Protection for Truck Drivers In the way you can not think</h3>
    <p class="blog-date">22 September 2019</p>
  </article>
</section>

<!-- testimonial -->
<section class="testimonial">
  <div class="abs" role="img" aria-label="Portrait photo of a customer in a denim shirt with arms crossed" style="left:199px;top:2666px;width:328px;height:410px;background:linear-gradient(180deg,#e7e7e9,#d9dbe0 55%,#4c6f9f)"></div>
  <h2 class="abs" style="left:572px;top:2770px;font-size:27px;font-weight:500;line-height:31px">Hear it from our<br>customers.</h2>
  <p class="body-copy abs" style="left:573px;top:2866px;width:400px;font-size:12.5px;line-height:21px;color:var(--navy)">Lorem ipsum dolor sit amet, consetetur sadipscing elitr, sed diam nonumy eirmod tempor invidunt ut labore et dolore magna aliquyam erat, sed diam voluptua. At vero eos et accusam et justo duo dolores et ea rebum. Stet clita kasd gubergren, no sea takimata sanctus</p>
  <p class="quote-name abs" style="left:573px;top:2970px">Arjun Mehta</p>
  <p class="quote-role abs" style="left:573px;top:2991px">UX/UI Designer</p>
</section>

<!-- contact -->
<section class="contact">
  <h2 class="abs" style="left:173px;top:3382px;font-size:37px;font-weight:500;line-height:45px">Contact Our<br>Team</h2>
  <p class="body-copy abs" style="left:173px;top:3487px;width:310px;font-size:12px;line-height:18px">Lorem ipsum dolor sit amet, consetetur sadipscing elitr, sed diam nonumy Lorem ipsum dolor sit amet, consetetur sadipscing</p>
  <form class="contact-card abs" style="left:550px;top:3348px;width:454px;height:433px">
    <div class="field" style="left:62px;top:48px;width:165px">First Name</div>
    <div class="field" style="left:238px;top:48px;width:165px">Last Name</div>
    <div class="field" style="left:62px;top:104px;width:341px">E-mail</div>
    <div class="field" style="left:62px;top:160px;width:341px">Phone</div>
    <div class="field" style="left:62px;top:217px;width:165px">Age</div>
    <div class="field" style="left:238px;top:217px;width:165px">Gender
      <svg style="position:absolute;right:12px;top:16px" width="12" height="8" viewBox="0 0 12 8" fill="none" stroke="var(--navy)" stroke-width="1.5"><path d="M1 1l5 5 5-5"/></svg>
    </div>
    <div class="field" style="left:62px;top:273px;width:341px">Cover Amount</div>
    <div class="btn-dark send-btn" style="position:absolute;left:62px;top:341px;width:341px;height:50px">Send Now</div>
  </form>
</section>

<!-- footer -->
<footer>
  <div class="footer-bg abs" style="left:0;top:3882px;width:1200px;height:245px"></div>
  <div class="abs" style="left:591px;top:3930px;width:18px;height:18px;border:2px solid var(--coral);border-radius:3px"></div>
  <div class="abs" style="left:600px;top:3962px;transform:translateX(-50%);font-size:14px">CoverCompare.life</div>
  <span class="footer-link abs" style="left:428px;top:4006px">Career</span>
  <span class="footer-link abs" style="left:494px;top:4006px">Privacy Policy</span>
  <span class="footer-link abs" style="left:582px;top:4006px">Terms of Services</span>
  <span class="footer-link abs" style="left:679px;top:4006px">Trust And Security</span>
  <span class="footer-link abs" style="left:761px;top:4006px">Contact Us</span>
  <span class="social abs" style="left:561px;top:4055px"></span>
  <span class="social abs" style="left:586px;top:4055px"></span>
  <span class="social abs" style="left:612px;top:4055px"></span>
  <span class="social abs" style="left:638px;top:4055px"></span>
  <span class="copyright abs" style="left:600px;top:4092px">Copyright 2019, All Rights Reserved By CoverCompare.life</span>
</footer>

</body>
</html>
```